Animal Eye Clinic needs a Business card

We are a new veterinary ophthalmology practice (Tessaly Animal Eye Care) and we need a business card designed. We only see animal eyes - we are not a regular veterinary clinic. We already have a logo. We are looking for a professional, good looking business card to hand out to our clients. We are looking for something simple but professional and contemporary. Our logo is likely the only picture/graphic that needs to be on the card.
Updates

Contact Information for Business Card

Marisol Dunkley, BSc, DVM, MSc, DipACVO
Veterinary Ophthalmologist

Phone: 250.418.3097
Email: tessalyanimaleyecare@mailbrook.net
Website: tessalyanimaleyecare.net
Address: 1840 Pellworth Rd
Kelowna, BC, V4T 8M3

Colors

Designer to choose colors to be used in the design.

Requirements
Must have
• Our logo (attached)

```html
<!DOCTYPE html>
<html lang="en">
<head>
<meta charset="utf-8">
<title>Tessaly Animal Eye Care – Business Card</title>
<link rel="stylesheet" href="https://fonts.googleapis.com/css2?family=Arimo:wght@400;700&family=Crimson+Text&family=Lato:wght@400&display=swap">
<style>
  :root {
    --backdrop: #c9c9c9;
    --teal: #0a8e9c;
    --teal-deep: #007d8b;
    --teal-light: #0a9bab;
    --ink: #5c5c5c;
    --ink-soft: #6a6a6a;
    --paper: #ffffff;
    --paper-shade: #ececec;
  }
  * { box-sizing: border-box; margin: 0; padding: 0; }
  html, body { width: 1200px; height: 1176px; overflow: hidden; }
  body { background: var(--backdrop); position: relative; }

  .card {
    position: absolute;
    left: 280px;
    width: 618px;
    height: 356px;
    border-radius: 22px;
    overflow: hidden;
  }

  /* Front */
  .card--front {
    top: 190px;
    background: linear-gradient(135deg, var(--paper-shade) 0%, var(--paper) 55%, #f4f4f4 100%);
  }
  .brand {
    position: absolute;
    left: 30px; top: 32px;
    display: flex; align-items: center; gap: 12px;
  }
  .brand__dot {
    width: 44px; height: 44px; border-radius: 50%;
    background: var(--teal);
  }
  .brand__name {
    font-family: "Arimo", sans-serif;
    font-weight: 700;
    font-size: 19px;
    color: var(--teal);
    letter-spacing: 0.5px;
  }
  .person { position: absolute; left: 30px; top: 175px; }
  .person__name {
    font-family: "Arimo", sans-serif;
    font-size: 22px; color: var(--ink);
    letter-spacing: 0.3px;
  }
  .person__creds { font-size: 15px; }
  .person__title {
    font-family: "Crimson Text", serif;
    font-size: 16.5px; color: var(--teal);
    margin-top: 2px;
  }
  .contact {
    position: absolute;
    font-family: "Lato", sans-serif;
    font-size: 15px; color: var(--ink-soft);
    line-height: 27px;
  }
  .contact--left { left: 30px; top: 253px; }
  .contact--right { right: 30px; top: 253px; text-align: right; }
  .contact__row { display: flex; align-items: center; gap: 9px; }
  .contact--right .contact__row { justify-content: flex-end; }
  .contact__row svg { width: 15px; height: 15px; fill: var(--teal); flex: none; }
  .contact__address-line { padding-right: 24px; }

  .web-band {
    position: absolute; left: 0; right: 0; bottom: 0;
    height: 36px;
    background: var(--teal);
    display: flex; align-items: center; justify-content: center;
    font-family: "Lato", sans-serif;
    font-size: 15px; letter-spacing: 2.4px;
    color: #e6f4f5;
  }

  /* Back */
  .card--back {
    top: 592px;
    background: linear-gradient(120deg, var(--teal-deep) 0%, var(--teal) 50%, var(--teal-light) 100%);
  }
  .back-mark {
    position: absolute;
    left: 157px; top: 76px;
    width: 200px; height: 200px; border-radius: 50%;
    background: #f2f4f4;
  }
  .back-name {
    position: absolute;
    left: 372px; top: 152px;
    font-family: "Arimo", sans-serif;
    font-weight: 700;
    font-size: 20px;
    line-height: 26px;
    color: var(--paper);
    letter-spacing: 0.5px;
  }
</style>
</head>
<body>

<section class="card card--front">
  <div class="brand">
    <span class="brand__dot"></span>
    <span class="brand__name">TESSALY ANIMAL EYE CARE</span>
  </div>

  <div class="person">
    <p class="person__name">MARISOL DUNKLEY, <span class="person__creds">BSC, DVM, MSC, DIPACVO</span></p>
    <p class="person__title">Veterinary Ophthalmologist</p>
  </div>

  <div class="contact contact--left">
    <p class="contact__row">
      <svg viewBox="0 0 24 24" aria-hidden="true"><path d="M12 5c-4.5 0-9 1.5-10 4v2h5V9c1.5-.6 3.3-.9 5-.9s3.5.3 5 .9v2h5V9c-1-2.5-5.5-4-10-4zM7 12l-3 6v2h16v-2l-3-6H7zm5 1.5a2.5 2.5 0 110 5 2.5 2.5 0 010-5z"/></svg>
      250.418.3097
    </p>
    <p class="contact__row">
      <svg viewBox="0 0 24 24" aria-hidden="true"><path d="M2 5h20v14H2V5zm2 2v.5l8 5.5 8-5.5V7H4zm0 3v7h16v-7l-8 5.5L4 10z"/></svg>
      tessalyanimaleyecare@mailbrook.net
    </p>
  </div>

  <div class="contact contact--right">
    <p class="contact__row">
      1840 Pellworth Rd
      <svg viewBox="0 0 24 24" aria-hidden="true"><path d="M12 2a7 7 0 00-7 7c0 5 7 13 7 13s7-8 7-13a7 7 0 00-7-7zm0 9.5A2.5 2.5 0 1112 6.5a2.5 2.5 0 010 5z"/></svg>
    </p>
    <p class="contact__address-line">Kelowna, BC, V4T 8M3</p>
  </div>

  <div class="web-band">tessalyanimaleyecare.net</div>
</section>

<section class="card card--back">
  <span class="back-mark"></span>
  <p class="back-name">TESSALY<br>ANIMAL EYE CARE</p>
</section>

</body>
</html>
```